Stationery and Business Card Design

We need stationary design for our new company pelvanta. Pelvanta is a company that provides city apartment rentals for tourists in Athens We need business cards, letterheads for A4 and A5 and envelopes for A4 A5. The design needs to be modern, friendly and corporate.

Target Market(s)

City Tourists

Industry/Entity Type

Tourism

```html
<!DOCTYPE html>
<html lang="en">
<head>
<meta charset="utf-8">
<title>Pelvanta Stationery Set</title>
<link rel="stylesheet" href="https://fonts.googleapis.com/css2?family=Raleway:wght@400;500;600&family=Ubuntu:wght@400;500&display=swap">
<style>
:root{
  --purple:#870c7c;
  --charcoal:#2d3335;
  --card-black:#1f1f1f;
  --paper:#ffffff;
  --ink:#111111;
  --muted:#444444;
  --faint:#eef1f1;
  --stage:#ffffff;
}
*{box-sizing:border-box;margin:0;padding:0}
html,body{width:1200px;height:1000px;overflow:hidden;background:var(--stage)}
body{position:relative;font-family:"Raleway",sans-serif}
.sheet{position:absolute;background:var(--paper);box-shadow:3px 4px 6px rgba(0,0,0,.45);overflow:hidden}
.brand{position:absolute;display:flex;flex-direction:column;align-items:center}
.brand-square{background:var(--purple)}
.brand-name{font-family:"Raleway",sans-serif;font-weight:500;color:var(--purple);line-height:1;white-space:nowrap;letter-spacing:-.5px}
.site-band{position:absolute;left:0;right:0;bottom:0;background:var(--charcoal);color:#fff;font-family:"Raleway",sans-serif;text-align:center;letter-spacing:.5px}
.item-label{position:absolute;left:0;right:0;text-align:center;font-family:"Ubuntu",sans-serif;color:var(--ink);line-height:1.25}
.contact{position:absolute;font-size:7px;color:var(--muted)}
.contact li{list-style:none;display:flex;align-items:center;gap:5px;height:15px}
.contact.right li{justify-content:flex-end;flex-direction:row}
.icon{width:10px;height:10px;border-radius:50%;background:var(--purple);display:inline-flex;align-items:center;justify-content:center;flex:none}
.icon svg{width:6px;height:6px}
.faint-mark{position:absolute;background:var(--faint)}
.envelope-window{position:absolute;border:1px solid #333;border-radius:6px}

/* cover */
.cover{left:25px;top:47px;width:385px;height:540px;background:var(--charcoal)}
.cover-frame{position:absolute;inset:7px;border:1.5px solid #e6e6e6}
.cover-title{position:absolute;top:52px;left:0;right:0;text-align:center;font-family:"Ubuntu",sans-serif;font-size:54px;color:#fff}
.cover .site{position:absolute;bottom:30px;left:0;right:0;text-align:center;color:#fff;font-size:13px;letter-spacing:.5px}

/* letterheads */
.side-strip{position:absolute;left:0;top:0;background:var(--purple)}
.side-strip-dark{position:absolute;left:0;background:var(--charcoal)}

/* business cards */
.card-dark{left:99px;top:605px;width:268px;height:162px;background:var(--card-black)}
.card-frame{position:absolute;inset:8px;border:1.5px solid #e6e6e6}
.card-light{left:99px;top:803px;width:268px;height:163px}
.holder-name{position:absolute;left:14px;top:27px;font-size:11px;font-weight:600;color:var(--purple)}
.holder-role{position:absolute;left:14px;top:42px;font-size:9px;color:var(--ink)}
.pointer{position:absolute;left:0;top:28px}
</style>
</head>
<body>

<!-- Cover -->
<section class="sheet cover">
  <div class="cover-frame"></div>
  <h1 class="cover-title">Cover</h1>
  <div class="brand" style="left:0;right:0;top:195px">
    <span class="brand-square" style="width:75px;height:75px"></span>
    <span class="brand-name" style="font-size:48px;margin-top:16px">Pelvanta</span>
  </div>
  <p class="site">www.pelvanta.com</p>
</section>

<!-- A4 Letterhead -->
<section class="sheet" style="left:428px;top:47px;width:350px;height:490px">
  <svg class="side-strip-svg" width="20" height="470" style="position:absolute;left:0;top:0" aria-hidden="true">
    <polygon points="0,0 6,0 6,400 0,412" fill="var(--purple)"/>
    <polygon points="0,418 12,404 8,470 0,470" fill="var(--charcoal)"/>
  </svg>
  <div class="brand" style="left:20px;top:15px;width:96px">
    <span class="brand-square" style="width:28px;height:28px"></span>
    <span class="brand-name" style="font-size:18px;margin-top:4px">Pelvanta</span>
  </div>
  <ul class="contact right" style="right:18px;top:21px">
    <li>000-0000-000 <span class="icon"><svg viewBox="0 0 10 10"><rect x="2.5" y="1" width="5" height="8" rx="1" fill="#fff"/></svg></span></li>
    <li>www.pelvanta@gmail.com <span class="icon"><svg viewBox="0 0 10 10"><rect x="1" y="2.5" width="8" height="5" fill="#fff"/></svg></span></li>
  </ul>
  <div class="faint-mark" style="left:80px;top:178px;width:190px;height:185px"></div>
  <p class="item-label" style="top:268px;font-size:32px">A4<br>Letterhead</p>
  <p class="site-band" style="height:30px;line-height:30px;font-size:11px">www.pelvanta.com</p>
</section>

<!-- A5 Letterhead -->
<section class="sheet" style="left:807px;top:60px;width:302px;height:427px">
  <svg width="20" height="400" style="position:absolute;left:0;top:0" aria-hidden="true">
    <polygon points="0,0 9,0 9,312 0,328" fill="var(--purple)"/>
    <polygon points="0,334 14,316 12,400 0,400" fill="var(--charcoal)"/>
  </svg>
  <div class="brand" style="left:28px;top:22px;width:96px">
    <span class="brand-square" style="width:26px;height:26px"></span>
    <span class="brand-name" style="font-size:18px;margin-top:4px">Pelvanta</span>
  </div>
  <ul class="contact right" style="right:22px;top:32px;font-size:8px">
    <li style="height:19px">000-0000-000 <span class="icon"><svg viewBox="0 0 10 10"><rect x="2.5" y="1" width="5" height="8" rx="1" fill="#fff"/></svg></span></li>
    <li style="height:19px">www.pelvanta@gmail.com <span class="icon"><svg viewBox="0 0 10 10"><rect x="1" y="2.5" width="8" height="5" fill="#fff"/></svg></span></li>
  </ul>
  <div class="faint-mark" style="left:72px;top:168px;width:158px;height:150px"></div>
  <p class="item-label" style="top:252px;font-size:32px">A5<br>Letterhead</p>
  <p class="site-band" style="height:29px;line-height:29px;font-size:13px">www.pelvanta.com</p>
</section>

<!-- Business card, front -->
<section class="sheet card-dark">
  <div class="card-frame"></div>
  <div class="brand" style="left:0;right:0;top:30px">
    <span class="brand-square" style="width:52px;height:52px"></span>
    <span class="brand-name" style="font-size:32px;margin-top:10px">Pelvanta</span>
  </div>
</section>

<!-- Business card, back -->
<section class="sheet card-light">
  <svg class="pointer" width="9" height="10" aria-hidden="true"><polygon points="0,0 5,0 9,5 5,10 0,10" fill="var(--card-black)"/></svg>
  <p class="holder-name">YOUR NAME</p>
  <p class="holder-role">Manager</p>
  <ul class="contact" style="left:14px;top:78px;font-size:7.5px;color:var(--ink)">
    <li style="height:17px"><span class="icon"><svg viewBox="0 0 10 10"><rect x="2.5" y="1" width="5" height="8" rx="1" fill="#fff"/></svg></span>000-0000-000</li>
    <li style="height:17px"><span class="icon"><svg viewBox="0 0 10 10"><rect x="1" y="2.5" width="8" height="5" fill="#fff"/></svg></span>www.pelvanta@gmail.com</li>
    <li style="height:17px"><span class="icon"><svg viewBox="0 0 10 10"><circle cx="5" cy="4.5" r="2.5" fill="#fff"/></svg></span>Your Address</li>
  </ul>
  <div class="brand" style="left:160px;top:73px;width:96px">
    <span class="brand-square" style="width:26px;height:26px"></span>
    <span class="brand-name" style="font-size:18px;margin-top:5px">Pelvanta</span>
  </div>
  <p class="site-band" style="height:25px;line-height:25px;font-size:8px;background:var(--card-black)">www.pelvanta.com</p>
</section>

<!-- A5 Envelope -->
<section class="sheet" style="left:428px;top:560px;width:297px;height:413px">
  <div class="brand" style="left:18px;top:20px;width:110px">
    <span class="brand-square" style="width:32px;height:32px"></span>
    <span class="brand-name" style="font-size:20px;margin-top:5px">Pelvanta</span>
  </div>
  <div class="envelope-window" style="left:18px;top:104px;width:180px;height:59px"></div>
  <p class="item-label" style="top:193px;left:10px;font-size:34px">A5<br>Envelope</p>
  <ul class="contact" style="left:18px;top:336px;font-size:7px">
    <li><span class="icon" style="width:8px;height:8px"><svg viewBox="0 0 10 10"><rect x="2.5" y="1" width="5" height="8" rx="1" fill="#fff"/></svg></span>000-0000-000</li>
    <li><span class="icon" style="width:8px;height:8px"><svg viewBox="0 0 10 10"><rect x="1" y="2.5" width="8" height="5" fill="#fff"/></svg></span>www.pelvanta@gmail.com</li>
    <li><span class="icon" style="width:8px;height:8px"><svg viewBox="0 0 10 10"><circle cx="5" cy="4.5" r="2.5" fill="#fff"/></svg></span>Your Address</li>
  </ul>
  <p class="site-band" style="height:27px;line-height:27px;font-size:13px">www.pelvanta.com</p>
</section>

<!-- A4 Envelope -->
<section class="sheet" style="left:797px;top:537px;width:328px;height:458px">
  <div class="brand" style="left:20px;top:24px;width:126px">
    <span class="brand-square" style="width:36px;height:36px"></span>
    <span class="brand-name" style="font-size:22px;margin-top:6px">Pelvanta</span>
  </div>
  <div class="envelope-window" style="left:20px;top:116px;width:199px;height:65px"></div>
  <p class="item-label" style="top:222px;left:20px;font-size:34px">A4<br>Envelope</p>
  <ul class="contact" style="left:20px;top:372px;font-size:7.5px">
    <li style="height:17px"><span class="icon"><svg viewBox="0 0 10 10"><rect x="2.5" y="1" width="5" height="8" rx="1" fill="#fff"/></svg></span>000-0000-000</li>
    <li style="height:17px"><span class="icon"><svg viewBox="0 0 10 10"><rect x="1" y="2.5" width="8" height="5" fill="#fff"/></svg></span>www.pelvanta@gmail.com</li>
    <li style="height:17px"><span class="icon"><svg viewBox="0 0 10 10"><circle cx="5" cy="4.5" r="2.5" fill="#fff"/></svg></span>Your Address</li>
  </ul>
  <p class="site-band" style="height:30px;line-height:30px;font-size:14px">www.pelvanta.com</p>
</section>

</body>
</html>
```